Harborline Restoration Business Card Design Phase 2

Professional and clean design. The design colors should flow with the logo. Two-sided card with the website on the back which is:

www.HarborlineRestoration.example.

"Specializing in Water Damage Restoration"

On the front I need the name, email, phone, and logo.

Name: Darnell Vickery
Email: Darnell@HarborlineRestoration.example
Phone: 555-018-2734 for now

I only have the Preview and Thumbnail right now but should have the source files uploaded within a day or two.

Target Market(s)

Flood victims, home owners with water damage from busted pipes etc...

Industry/Entity Type

Business

Contact Information for Business Card

Name: Darnell Vickery

Font styles to use
Serif
Sans Serif

Requirements
Must have
• Business Card Details Info

```html
<!DOCTYPE html>
<html lang="en">
<head>
<meta charset="utf-8">
<title>Harborline Restoration – Business Card</title>
<link rel="stylesheet" href="https://fonts.googleapis.com/css2?family=Oswald:wght@500;600&family=Open+Sans:wght@400&display=swap">
<style>
  :root {
    --navy: #1d3a63;
    --navy-deep: #1a365d;
    --green: #4d9a3c;
    --card-white: #fbfbfb;
    --backdrop: #e9e6e1;
  }
  * { box-sizing: border-box; margin: 0; padding: 0; }
  html, body {
    width: 1200px;
    height: 1023px;
    overflow: hidden;
    background: var(--backdrop);
  }
  .canvas {
    position: relative;
    width: 1200px;
    height: 1023px;
  }
  .card {
    position: absolute;
    left: 220px;
    width: 760px;
    height: 434px;
    box-shadow: 0 6px 18px rgba(0,0,0,0.18);
  }
  .card--front { top: 60px; background: var(--card-white); }
  .card--back  { top: 540px; background: var(--navy-deep); }

  .brand {
    position: absolute;
    left: 56px;
    top: 70px;
    display: flex;
    align-items: center;
    gap: 16px;
  }
  .brand__mark {
    width: 34px;
    height: 34px;
    background: var(--navy);
  }
  .brand__name {
    font-family: 'Oswald', sans-serif;
    font-weight: 600;
    font-size: 52px;
    line-height: 1;
    text-transform: uppercase;
    letter-spacing: 0.5px;
    color: var(--navy);
  }
  .contact {
    position: absolute;
    left: 56px;
    bottom: 56px;
  }
  .contact__name {
    font-family: 'Oswald', sans-serif;
    font-weight: 600;
    font-size: 26px;
    text-transform: uppercase;
    color: var(--navy);
    margin-bottom: 10px;
  }
  .contact__line {
    font-family: 'Open Sans', sans-serif;
    font-size: 19px;
    line-height: 1.55;
    color: var(--green);
  }

  .back-copy {
    position: absolute;
    left: 0;
    right: 0;
    top: 150px;
    text-align: center;
    font-family: 'Open Sans', sans-serif;
    font-size: 22px;
    line-height: 1.7;
    color: var(--green);
  }
</style>
</head>
<body>
<main class="canvas">
  <section class="card card--front" aria-label="Business card front">
    <div class="brand">
      <span class="brand__mark"></span>
      <span class="brand__name">Harborline Restoration</span>
    </div>
    <div class="contact">
      <p class="contact__name">Darnell Vickery</p>
      <p class="contact__line">Darnell@HarborlineRestoration.example</p>
      <p class="contact__line">555-018-2734 for now</p>
    </div>
  </section>

  <section class="card card--back" aria-label="Business card back">
    <div class="back-copy">
      <p class="back-copy__web">www.HarborlineRestoration.example</p>
      <p class="back-copy__tagline">Specializing In Water Damage Restoration</p>
    </div>
  </section>
</main>
</body>
</html>
```